Move the hackers to Wordpress

Yep, we want to move https://www.tallowmarsh.com/ to Wordpress. It'll make it easier to update and add content. I'd like mostly the same look, but I'm not stuck with it.
Updates

DO NOT RESPOND OUTSIDE OF PIXEL HARBOR OR CONTACT US DIRECTLY.

Industry/Entity Type

Computer Security

Coding

Coded - Design and coding required

Font styles to use
Sans Serif

Colors
ec1f27

Requirements
Must have
• What I do want is:
• 1. Similar look to the existing site
• 2. Needs to work on one of the Wordpress hosting sites. I do NOT want to run my own Wordpress server.
• 3. Keep the animation in the top panel.
• 4. Mobile support
• The rest can be changed as needed.
Nice to have
• I like the transitions when the "services" panel shows up. Not stuck on it, but it is a nice touch.

```html
<!DOCTYPE html>
<html lang="en">
<head>
<meta charset="utf-8">
<title>Tallow Marsh — Offensive Services</title>
<link rel="stylesheet" href="https://fonts.googleapis.com/css2?family=Roboto:wght@400;500;700&family=Open+Sans:wght@400;600&display=swap">
<style>
:root{
  --red:#ec1f27;
  --red-deep:#b5121b;
  --ink:#111111;
  --night:#14171c;
  --night-2:#262a31;
  --text:#555a60;
  --white:#ffffff;
  --line:#d9d9d9;
}
*{box-sizing:border-box;margin:0;padding:0}
html,body{width:1200px;height:2795px;overflow:hidden}
body{position:relative;background:var(--white);font-family:"Open Sans",Arial,sans-serif;color:var(--text)}
.heading{font-family:"Roboto",Arial,sans-serif}
.abs{position:absolute}
.bands{position:absolute;left:0;top:0;width:1200px;height:2795px}

/* header */
.site-header{position:absolute;left:0;top:0;width:1200px;height:104px;background:var(--white);z-index:2}
.brand{position:absolute;display:flex;align-items:center;gap:12px;font-family:"Roboto",Arial,sans-serif;font-weight:700;color:var(--ink);letter-spacing:2px}
.brand-mark{width:28px;height:28px;background:var(--red)}
.site-header .brand{left:130px;top:28px;font-size:30px}
.main-nav{position:absolute;left:452px;top:40px;display:flex;gap:0;font-family:"Roboto",Arial,sans-serif;font-weight:500;font-size:17px;color:var(--ink)}
.main-nav a{color:inherit;text-decoration:none;position:absolute;white-space:nowrap}
.main-nav .is-active{color:var(--red)}
.cta{position:absolute;left:872px;top:24px;width:200px;height:56px;border-radius:28px;background:var(--red);color:var(--white);font-family:"Roboto",Arial,sans-serif;font-weight:500;font-size:15px;line-height:18px;padding:10px 0 0 20px}
.cta-avatar{position:absolute;right:5px;top:5px;width:46px;height:46px;border-radius:50%;background:linear-gradient(#e9d4c4,#c9a996);border:3px solid var(--white)}

/* hero */
.hero-mark{left:576px;top:212px;width:48px;height:48px;background:var(--red)}
.hero-title{left:0;top:305px;width:1200px;text-align:center;font-weight:700;font-size:50px;line-height:64px;color:var(--white)}
.accent{color:var(--red)}

/* what we do */
.intro{left:130px;top:640px;width:452px}
.section-title{font-weight:400;font-size:32px;color:var(--ink)}
.intro-lead{font-family:"Roboto",Arial,sans-serif;font-weight:700;font-size:14px;line-height:20px;color:var(--ink);margin-top:8px}
.intro-body{font-size:14.5px;line-height:23px;margin-top:30px;text-align:justify}
.btn{display:inline-flex;align-items:center;gap:22px;margin-top:18px;height:46px;padding:0 24px;border-radius:23px;background:var(--red);color:var(--white);font-family:"Roboto",Arial,sans-serif;font-size:15px}
.intro-visual{left:712px;top:652px;width:320px;height:320px;border-radius:50%;background:radial-gradient(circle at 70% 65%,var(--red) 0 30%,rgba(236,31,39,.12) 31% 100%)}

/* services */
.services-title{left:0;top:1140px;width:1200px;text-align:center;font-weight:400;font-size:32px;color:var(--white)}
.service{top:1222px;width:330px;text-align:center;color:var(--white)}
.service svg{display:block;margin:0 auto}
.service-name{font-family:"Roboto",Arial,sans-serif;font-weight:700;font-size:18px;line-height:25px;margin-top:20px}
.service-text{font-size:11.5px;line-height:22px;margin-top:22px;padding:0 14px}
.slider-dots{left:578px;top:1622px}

/* about */
.about-title{left:0;top:1800px;width:1200px;text-align:center}
.about-lead{left:400px;top:1858px;width:400px;text-align:center;font-size:15px;line-height:24px}
.about-media{left:130px;top:1962px;width:458px;height:308px;background:linear-gradient(135deg,#8a7458,#c6b49a 45%,#5d6a78)}
.play{left:330px;top:2088px}
.reviewer-photo{left:794px;top:1993px;width:84px;height:84px;border-radius:50%;background:linear-gradient(#d9dde2,#9aa3ad)}
.reviewer-name{left:636px;top:2096px;width:400px;text-align:center;font-family:"Roboto",Arial,sans-serif;font-weight:500;font-size:17px;color:#444}
.reviewer-quote{left:666px;top:2140px;width:340px;text-align:center;font-size:14.5px;line-height:24px}

/* footer */
.site-footer .brand{left:130px;top:2432px;font-size:28px;color:var(--white)}
.footer-tag{left:130px;top:2498px;font-family:"Roboto",Arial,sans-serif;font-size:21px;line-height:29px;color:var(--white)}
.social{left:130px;top:2572px;display:flex;gap:9px}
.social span{width:33px;height:33px;border-radius:50%}
.footer-heading{font-family:"Roboto",Arial,sans-serif;font-weight:700;font-size:19px;color:var(--white)}
.quick-links{left:552px;top:2428px}
.quick-links ul{list-style:none;margin-top:22px}
.quick-links li,.contact li{display:flex;align-items:center;gap:14px;font-family:"Roboto",Arial,sans-serif;font-size:14.5px;color:var(--white);height:39px}
.contact{left:855px;top:2428px}
.contact ul{list-style:none;margin-top:22px}
.copyright{left:110px;top:2750px;font-family:"Roboto",Arial,sans-serif;font-size:15px;color:#555}
</style>
</head>
<body>

<svg class="bands" viewBox="0 0 1200 2795" aria-hidden="true">
  <defs>
    <linearGradient id="nightFill" x1="0" y1="0" x2="0" y2="1">
      <stop offset="0" stop-color="#0f1216"/><stop offset="1" stop-color="#2b3038"/>
    </linearGradient>
    <linearGradient id="redFill" x1="0" y1="0" x2="1" y2="1">
      <stop offset="0" stop-color="#c7121c"/><stop offset=".5" stop-color="#ec1f27"/><stop offset="1" stop-color="#a80d16"/>
    </linearGradient>
    <linearGradient id="footFill" x1="0" y1="0" x2="1" y2="1">
      <stop offset="0" stop-color="#1b1b1d"/><stop offset="1" stop-color="#050506"/>
    </linearGradient>
  </defs>
  <polygon points="0,104 1200,104 1200,520 0,587" fill="url(#nightFill)"/>
  <polygon points="0,1118 1200,1072 1200,1686 0,1733" fill="url(#redFill)"/>
  <polygon points="0,2386 1200,2370 1200,2708 0,2684" fill="url(#footFill)"/>
</svg>

<header class="site-header">
  <div class="brand"><span class="brand-mark"></span>TALLOW MARSH</div>
  <nav class="main-nav">
    <a style="left:0">SERVICES</a>
    <a style="left:118px">BLOG</a>
    <a style="left:202px">PRESS</a>
    <a class="is-active" style="left:295px">CONTACT</a>
  </nav>
  <a class="cta">Contact One of<br>our Expert today<span class="cta-avatar" role="img" aria-label="Portrait of a team expert"></span></a>
</header>

<section class="hero">
  <div class="abs hero-mark"></div>
  <h1 class="abs heading hero-title"><span class="accent">OFFENSIVE</span> SERVICES<br>FROM <span class="accent">OFFENSIVE</span> MINDS</h1>
</section>

<section class="what-we-do">
  <div class="abs intro">
    <h2 class="heading section-title">WHAT WE DO</h2>
    <p class="intro-lead">We are an information security company focusing on real world threats.</p>
    <p class="intro-body">Tallow Marsh is an information security consulting company that concentrates on the latest threats to organizations today. We perform in-depth analysis, determine organization/business risk, and find the vulnerabilities before the bad guys do. Our team includes internationally renowned experts who have been featured in international news outlets and conferences, including The Harbor Ledger, The Capital Courier, a Meridian Channel Asia Documentary.</p>
    <a class="btn">Read More
      <svg width="16" height="16" viewBox="0 0 16 16"><rect x="3" y="3" width="10" height="10" transform="rotate(45 8 8)" fill="none" stroke="#fff" stroke-width="1.5"/></svg>
    </a>
  </div>
  <div class="abs intro-visual" role="img" aria-label="Illustration of a globe with a security bug badge"></div>
</section>

<section class="services">
  <h2 class="abs heading services-title">Services</h2>

  <article class="abs service" style="left:116px">
    <svg width="116" height="116" viewBox="0 0 116 116"><rect x="24" y="24" width="68" height="68" rx="4" transform="rotate(45 58 58)" fill="none" stroke="#fff" stroke-width="2.5"/><path d="M46 50 A15 15 0 1 1 47 66" fill="none" stroke="#fff" stroke-width="2.5"/><path d="M42 44 L46 51 L53 47" fill="none" stroke="#fff" stroke-width="2.5"/></svg>
    <h3 class="service-name">Internal Pivot Assessment &amp;<br>Post Exploitation</h3>
    <p class="service-text">We start as a low privilege user and attempt to move through the network in an attempt to access the data that matters to you. This is a simulation of a rogue trusted insider or a compromised internal host. We determine your risk when the egg shell is cracked. Even a seemingly insignificant compromise can have big consequences, and our goal is to demonstrate this risk.</p>
  </article>

  <article class="abs service" style="left:435px">
    <svg width="116" height="116" viewBox="0 0 116 116"><rect x="24" y="24" width="68" height="68" rx="4" transform="rotate(45 58 58)" fill="none" stroke="#fff" stroke-width="2.5"/><g fill="none" stroke="#fff" stroke-width="2.2"><circle cx="58" cy="51" r="6"/><circle cx="44" cy="54" r="5"/><circle cx="72" cy="54" r="5"/><path d="M47 70 a11 10 0 0 1 22 0 Z"/><path d="M35 68 a9 8 0 0 1 13 -6"/><path d="M81 68 a9 8 0 0 0 -13 -6"/></g></svg>
    <h3 class="service-name">Red Team Adversary<br>Simulation</h3>
    <p class="service-text">A goal-based assessment where we attack just like a real world adversary. This includes external attacks and targeted phishing to demonstrate the real risk to your data.</p>
  </article>

  <article class="abs service" style="left:753px">
    <svg width="116" height="116" viewBox="0 0 116 116"><rect x="24" y="24" width="68" height="68" rx="4" transform="rotate(45 58 58)" fill="none" stroke="#fff" stroke-width="2.5"/><g fill="none" stroke="#fff" stroke-width="2.2"><circle cx="58" cy="58" r="6"/><path d="M55 42 h6 l1 5 4 2 4-3 4 4-3 4 2 4 5 1 v6 l-5 1-2 4 3 4-4 4-4-3-4 2-1 5 h-6 l-1-5-4-2-4 3-4-4 3-4-2-4-5-1 v-6 l5-1 2-4-3-4 4-4 4 3 4-2 Z"/></g></svg>
    <h3 class="service-name">Penetration Testing &amp;<br>Vulnerability Assessments</h3>
    <p class="service-text">This includes vulnerability scans of the in-scope systems where we manually verify issues and exploit any issues found. We report on the issues that actually have a real risk to your organization.</p>
  </article>

  <svg class="abs slider-dots" width="44" height="20" viewBox="0 0 44 20" aria-hidden="true"><rect x="5" y="5" width="10" height="10" transform="rotate(45 10 10)" fill="none" stroke="#fff" stroke-width="1.6"/><rect x="25" y="5" width="10" height="10" transform="rotate(45 30 10)" fill="#fff"/></svg>
</section>

<section class="about">
  <h2 class="abs heading section-title about-title">ABOUT US</h2>
  <p class="abs about-lead">We focus on hacking. This is our passion. We find the vulnerabilities before the bad guys do.</p>
  <div class="abs about-media" role="img" aria-label="Video still of a team working at laptops on a wooden desk"></div>
  <svg class="abs play" width="58" height="58" viewBox="0 0 58 58" aria-hidden="true"><circle cx="29" cy="29" r="29" fill="rgba(255,255,255,.85)"/><path d="M23 18 L40 29 L23 40 Z" fill="#333"/></svg>
  <div class="abs reviewer-photo" role="img" aria-label="Client portrait"></div>
  <p class="abs reviewer-name">D.H. (Undisclosed Organization)</p>
  <p class="abs reviewer-quote">I read the report yesterday. This is one of the best-written, actionable pentest reports I've ever seen.</p>
</section>

<footer class="site-footer">
  <div class="brand"><span class="brand-mark"></span>TALLOW MARSH</div>
  <p class="abs footer-tag"><span class="accent">OFFENSIVE</span> SERVICES<br>FROM <span class="accent">OFFENSIVE</span> MINDS</p>
  <div class="abs social" aria-label="Social profiles">
    <span style="background:#3b5998"></span><span style="background:#1da1f2"></span><span style="background:#d93b2b"></span><span style="background:#0e76a8"></span>
  </div>

  <div class="abs quick-links">
    <h3 class="footer-heading">Quick Links</h3>
    <ul>
      <li><svg width="16" height="16" viewBox="0 0 16 16"><rect x="3" y="3" width="10" height="10" transform="rotate(45 8 8)" fill="none" stroke="#ec1f27" stroke-width="1.5"/></svg>HOME</li>
      <li><svg width="16" height="16" viewBox="0 0 16 16"><rect x="3" y="3" width="10" height="10" transform="rotate(45 8 8)" fill="none" stroke="#ec1f27" stroke-width="1.5"/></svg>ABOUT</li>
      <li><svg width="16" height="16" viewBox="0 0 16 16"><rect x="3" y="3" width="10" height="10" transform="rotate(45 8 8)" fill="none" stroke="#ec1f27" stroke-width="1.5"/></svg>SERVICES</li>
      <li><svg width="16" height="16" viewBox="0 0 16 16"><rect x="3" y="3" width="10" height="10" transform="rotate(45 8 8)" fill="none" stroke="#ec1f27" stroke-width="1.5"/></svg>CONTACT</li>
    </ul>
  </div>

  <div class="abs contact">
    <h3 class="footer-heading">Contact Us</h3>
    <ul>
      <li><svg width="26" height="18" viewBox="0 0 26 18"><rect x="1" y="1" width="24" height="16" fill="none" stroke="#ec1f27" stroke-width="1.5"/><path d="M1 1 L13 10 L25 1" fill="none" stroke="#ec1f27" stroke-width="1.5"/></svg>contact@tallowmarsh.com</li>
      <li><svg width="26" height="20" viewBox="0 0 26 20"><path d="M5 2 l4 0 2 5-3 2 a12 12 0 0 0 6 6 l2-3 5 2 0 4 a2 2 0 0 1-2 2 A17 17 0 0 1 3 4 a2 2 0 0 1 2-2 Z" fill="none" stroke="#ec1f27" stroke-width="1.5"/></svg>+1.555.014.2290</li>
    </ul>
  </div>

  <p class="abs copyright">© 2018 Company Name&nbsp; All right reserved</p>
</footer>

</body>
</html>
```